Medical Waste Company with Logo

Need a business card design that targets office managers in the medical community. This card will be the front line for our sales team to market our services to the community. We would like to have email, phone number, website. Please use the logo attached to create a design that we would be proud of.

Target Market(s)

Medical Clients

Industry/Entity Type

Medical Supply

Contact Information for Business Card

Please use logo attached

Colors

Designer to choose colors to be used in the design.

Requirements
Must have
• Our logo (see attached file)
Nice to have
• Maybe a pop of some sort, raised..?

```html
<!DOCTYPE html>
<html lang="en">
<head>
<meta charset="utf-8">
<title>Northpeak Clinical Disposal – Business Card</title>
<link href="https://fonts.googleapis.com/css2?family=Roboto:wght@400;500;700&display=swap" rel="stylesheet">
<style>
  :root {
    --backdrop: #8c8c8e;
    --card: #f3f3f5;
    --brand-blue: #17407f;
    --ink: #1f1f22;
    --rule: #b9babe;
    --emboss: #d3d4d9;
  }
  * { box-sizing: border-box; margin: 0; padding: 0; }
  html, body {
    width: 1200px;
    height: 1101px;
    overflow: hidden;
    background: var(--backdrop);
    font-family: "Roboto", Arial, sans-serif;
  }
  .card {
    position: absolute;
    left: 50px;
    top: 246px;
    width: 1100px;
    height: 609px;
    background: var(--card);
  }
  .brand-name {
    position: absolute;
    left: 585px;
    top: 150px;
    width: 430px;
    text-align: center;
    font-weight: 500;
    font-size: 40px;
    line-height: 48px;
    letter-spacing: 1px;
    color: var(--emboss);
    text-transform: uppercase;
  }
  .person {
    position: absolute;
    left: 94px;
    top: 310px;
  }
  .person-name {
    font-weight: 700;
    font-size: 41px;
    line-height: 50px;
    color: var(--brand-blue);
    letter-spacing: -0.3px;
  }
  .person-title {
    font-weight: 400;
    font-size: 26px;
    line-height: 34px;
    color: var(--ink);
  }
  .divider {
    position: absolute;
    left: 90px;
    top: 418px;
    width: 929px;
    height: 1.5px;
    background: var(--rule);
  }
  .contact-list {
    position: absolute;
    left: 90px;
    top: 440px;
    list-style: none;
  }
  .contact-item {
    display: flex;
    align-items: center;
    height: 39px;
    font-size: 26px;
    color: var(--ink);
  }
  .contact-icon {
    width: 26px;
    height: 26px;
    margin-right: 18px;
    flex: none;
  }
  .address {
    position: absolute;
    right: 81px;
    top: 440px;
    text-align: right;
    font-style: normal;
    font-size: 26px;
    line-height: 39px;
    color: var(--ink);
  }
</style>
</head>
<body>
  <main class="card">
    <div class="brand-name">Northpeak Clinical<br>Disposal</div>

    <section class="person">
      <h1 class="person-name">Daniel Harper</h1>
      <p class="person-title">Managing Director</p>
    </section>

    <div class="divider"></div>

    <ul class="contact-list">
      <li class="contact-item">
        <svg class="contact-icon" viewBox="0 0 24 24" aria-hidden="true">
          <path fill="var(--brand-blue)" d="M6.6 2.5c.5-.3 1.1-.2 1.4.3l2 3.2c.3.5.2 1.1-.2 1.4L8.4 8.6c.9 2.6 3.2 5.3 5.8 6.6l1.3-1.4c.4-.4 1-.5 1.4-.2l3.3 1.8c.5.3.7.9.4 1.4l-1.1 2.2c-.5 1-1.6 1.6-2.7 1.4C10 19.4 4.8 13.6 3.9 7c-.1-1.1.4-2.2 1.4-2.8z"/>
        </svg>
        <span>250 555 0142</span>
      </li>
      <li class="contact-item">
        <svg class="contact-icon" viewBox="0 0 24 24" aria-hidden="true">
          <rect x="2" y="5" width="20" height="14" fill="none" stroke="var(--brand-blue)" stroke-width="1.6"/>
          <path d="M2 5l10 8 10-8M2 19l7.5-7M22 19l-7.5-7" fill="none" stroke="var(--brand-blue)" stroke-width="1.6"/>
        </svg>
        <span>daniel@northpeakclinical.com</span>
      </li>
      <li class="contact-item">
        <svg class="contact-icon" viewBox="0 0 24 24" aria-hidden="true">
          <g fill="none" stroke="var(--brand-blue)" stroke-width="1.5">
            <circle cx="12" cy="12" r="10"/>
            <ellipse cx="12" cy="12" rx="4.5" ry="10"/>
            <path d="M2 12h20M3.5 7h17M3.5 17h17M12 2v20"/>
          </g>
        </svg>
        <span>www.northpeakclinical.com</span>
      </li>
    </ul>

    <address class="address">
      48 Harbour Row Suite 210<br>
      Kelowna<br>
      BC V1Y2K4
    </address>
  </main>
</body>
</html>
```